Website for Veteran Air Force Plumbing Combany

Project:
current site: talvikcrew.com
Growing plumbing company in need of a new homepage and inner page template (2 PSDs). Their goal for their style would be to have distinct areas that direct to their main menu items (Service Areas, Services, Sewer & Drain Cleaning, Blog) (example competitor site: http://larkfieldpipefixers.com/).

Homepage:

Theme: Masculine, Air Force veteran, plumbing, honest up-front pricing, free estimates

1. Style distinct areas
a. Top phone numbers with area served (High priority for customer)
i. Fort Myers: (555) 318-4702
Estero: (555) 318-4702
Naples: (555) 726-1059
Bonita Springs: (555) 726-1059
b. Social Buttons (chatterly, quipster, vidnook, careerloop, zorbo+)
i. Separate Quipster Follow button
c. Logo
d. 24 HR Emergency plumber CTA button
e. Menu
f. Slider with cta buttons
g. Video spot
h. Testimonials
i. Chatterly page plugin spot
j. Quick contact form (email address, small paragraph, send button)
k. Coupons
l. Page Title & Welcome paragraph
m. service columns with action buttons
n. Marla's list & QT Rating action buttons
o. Footer

Inner page:
1. Page title
2. Content section
3. Side bar section
a. video spot
b. Zorbo testimonial plugin spot
c. video2 spot
d. Marla's List & QT Rating action buttons

Target Market(s)

Home owners and construction managers

Industry/Entity Type

It Company

Number of Pages Required

2 page

Requirements
Must have
• Clear distinct areas for information
• Prominent area/phone number

```html
<!DOCTYPE html>
<html lang="en">
<head>
<meta charset="utf-8">
<title>Talvik Crew Plumbing & Drain</title>
<link href="https://fonts.googleapis.com/css2?family=Oswald:wght@400;500;700&family=Roboto+Condensed:ital,wght@0,400;0,700;1,700&family=Open+Sans:wght@400;600;700&display=swap" rel="stylesheet">
<style>
:root{
  --red:#d11f26;--red-dark:#a5161b;--ink:#222;--dark:#2b2b2b;--darker:#1c1c1c;
  --grey:#f1f1f1;--line:#dcdcdc;--blue:#0f3d7a;--blue-dark:#0a2a57;--text:#555;--white:#fff;--green:#3a8f3a;
}
*{box-sizing:border-box;margin:0;padding:0}
html,body{width:1200px;height:3700px;overflow:hidden}
body{font-family:"Open Sans",Arial,sans-serif;color:var(--text);font-size:13px;background:#fff}
.wrap{width:1080px;margin:0 auto;position:relative}
h2.sec{font-family:"Roboto Condensed",Arial,sans-serif;font-style:italic;font-weight:700;font-size:30px;color:var(--ink);display:flex;align-items:center;gap:10px}
h2.sec .hl{color:var(--red)}
.star{width:22px;height:22px;fill:var(--red)}
.btn{display:inline-block;background:var(--red);color:#fff;font-family:"Oswald",sans-serif;font-size:14px;text-transform:uppercase;padding:10px 22px;border-radius:3px}
.btn.dark{background:#444}
.ph{background:linear-gradient(135deg,#8c8c8c,#c9c9c9)}
.topbar{height:32px;background:var(--darker);color:#ddd;font-size:12px}
.topbar .wrap{display:flex;align-items:center;height:32px;justify-content:space-between}
.topbar .big{font-family:"Oswald",sans-serif;font-size:18px;color:#fff}
.topbar .nums{display:flex;gap:22px}
.topbar .nums b{color:#fff}
.social{display:flex;gap:5px}
.social span{width:20px;height:20px;background:var(--red);border-radius:3px}
.header{height:128px}
.header .wrap{display:flex;align-items:center;justify-content:space-between;height:128px}
.logo{display:flex;align-items:center;gap:12px}
.logo .dot{width:60px;height:60px;border-radius:50%;background:var(--red)}
.logo .name{font-family:"Oswald",sans-serif;font-weight:700;font-size:30px;color:var(--ink);line-height:1.05;text-transform:uppercase}
.hbtns{display:flex;gap:14px}
.chat{border:2px solid var(--ink);color:var(--ink);font-family:"Oswald",sans-serif;font-size:13px;padding:8px 18px;border-radius:3px;text-align:center;line-height:1.2}
.nav{height:36px;background:var(--red)}
.nav ul{list-style:none;display:flex;justify-content:flex-end;height:36px;align-items:center}
.nav li{color:#fff;font-family:"Oswald",sans-serif;font-size:14px;padding:0 16px;border-left:1px solid rgba(255,255,255,.3)}
.hero{height:444px;position:relative;background:linear-gradient(120deg,#3d4c5c,#9aa7b3 55%,#d7dde2)}
.hero .cap{position:absolute;left:590px;top:150px;width:490px;color:#fff}
.hero .cap h1{font-family:"Oswald",sans-serif;font-size:38px;font-weight:500;background:rgba(0,0,0,.55);padding:4px 14px;display:inline-block;white-space:nowrap}
.hero .cap p{background:rgba(0,0,0,.45);padding:8px 14px;font-size:13px;margin:8px 0 14px}
.hero .dots{position:absolute;bottom:16px;left:50%;display:flex;gap:6px;transform:translateX(-50%)}
.hero .dots span{width:10px;height:10px;border-radius:50%;background:#fff;opacity:.6}
.ratings{padding:46px 0 40px}
.ratings .wrap{display:flex;gap:60px}
.rate{flex:1}
.rate .row{display:flex;gap:20px;margin:20px 0 14px;align-items:center}
.badge{width:110px;height:70px;background:#e6e6e6;border-radius:4px}
.badge.b{background:var(--blue);width:70px}
.rate a{color:var(--blue);font-size:12px}
.tv{background:var(--grey);padding:44px 0 50px;border-top:1px solid var(--line)}
.tv .wrap{display:flex;gap:60px}
.tv .col{flex:1}
.tcard{background:#fff;border:1px solid var(--line);border-radius:4px;padding:18px 20px;margin-top:18px;display:flex;gap:18px}
.tcard .av{width:64px;height:64px;border-radius:50%;background:#c9b6a5;flex:none}
.tcard p{font-style:italic;font-size:12px;line-height:1.6}
.tcard .who{margin-top:6px;font-size:12px;color:var(--ink)}
.stars{color:var(--red);font-size:14px}
.video{margin-top:18px;height:280px;background:linear-gradient(135deg,#394754,#7b8896);position:relative;border-radius:2px}
.play{position:absolute;left:50%;top:50%;width:60px;height:42px;margin:-21px 0 0 -30px;background:rgba(0,0,0,.7);border-radius:8px}
.play:after{content:"";position:absolute;left:24px;top:12px;border-left:16px solid #fff;border-top:9px solid transparent;border-bottom:9px solid transparent}
.vbar{position:absolute;left:0;right:0;bottom:0;height:30px;background:rgba(0,0,0,.6)}
.vtitle{position:absolute;left:12px;top:10px;color:#fff;font-size:13px}
.welcome{padding:40px 0}
.welcome .wrap{display:flex;gap:50px}
.welcome .main{flex:1}
.welcome h2{font-family:"Roboto Condensed",sans-serif;font-style:italic;font-size:30px;color:var(--red)}
.welcome h3{font-family:"Oswald",sans-serif;font-size:30px;color:var(--ink);text-transform:uppercase;margin:4px 0 16px}
.welcome p{line-height:1.75;margin-bottom:14px}
.ribbon{display:inline-block;background:var(--red);color:#fff;font-family:"Roboto Condensed",sans-serif;font-style:italic;font-weight:700;font-size:20px;padding:10px 24px;margin:10px 0 16px}
.form{width:300px;background:#ebebeb;border-radius:4px;overflow:hidden}
.form h4{background:var(--red);color:#fff;font-family:"Roboto Condensed",sans-serif;font-style:italic;font-size:24px;padding:10px 18px}
.form .in{padding:14px 18px}
.form .note{text-align:center;font-size:12px;margin-bottom:10px}
.field{height:34px;background:#fff;border:1px solid var(--line);margin-bottom:9px;font-size:11px;color:#999;padding:9px 10px}
.field.ta{height:80px}
.captcha{height:44px;background:#ddd;margin-bottom:10px}
.services{background:#262626;padding:40px 0;height:400px}
.services h2.sec{color:#fff}
.cards{display:flex;gap:14px;margin-top:28px}
.card{flex:1;background:#fff}
.card .img{height:120px}
.card .lbl{display:flex;gap:10px;padding:12px;align-items:center}
.card .lbl i{width:34px;height:34px;background:var(--red);flex:none}
.card .lbl span{font-family:"Oswald",sans-serif;font-size:14px;color:var(--ink);text-transform:uppercase;line-height:1.2}
.center{text-align:center;margin-top:26px}
.why{height:520px;background:linear-gradient(160deg,var(--blue) 0%,var(--blue-dark) 100%);color:#dfe7f2;padding:36px 0}
.why h2.sec{color:#fff}
.why .wrap>.cols{display:flex;gap:50px;margin-top:20px}
.why .lead{font-size:18px;color:#fff;margin-bottom:12px;line-height:1.4}
.why ul{list-style:none;line-height:1.85}
.why li:before{content:"✓ ";color:#fff}
.why .vid{width:530px}
.why .vid .video{height:300px;margin:0}
.why .vid p{margin-top:14px;line-height:1.6;font-size:12px}
.why .ribbon{margin-top:20px}
.plugins{height:320px;background:var(--grey);padding:34px 0}
.plugins .wrap{display:flex;gap:24px}
.pl{flex:1;background:#fff;border:1px solid var(--line);min-height:240px}
.pl h5{font-size:12px;color:var(--ink);padding:8px 12px;border-bottom:1px solid var(--line)}
.pl .it{display:flex;gap:10px;padding:10px 12px;font-size:11px;line-height:1.5}
.pl .it i{width:34px;height:34px;background:#ccc;flex:none}
.footer{height:480px;background:var(--darker);color:#bbb;padding:44px 0}
.footer .wrap{display:flex;gap:46px}
.footer h2.sec{color:#fff;font-size:26px}
.fcol{flex:1}
.map{height:220px;margin-top:16px;background:linear-gradient(135deg,#7aa4c9,#b7c8a3)}
.areas{width:150px;margin-left:auto;margin-top:-180px;position:relative;background:#fff;color:var(--ink);font-size:11px;line-height:1.9;padding:8px 12px}
.ff{height:32px;background:#fff;margin-top:10px}
.ff.ta{height:80px}
.footer .btn{margin-top:12px}
.cd{margin-top:18px;line-height:2.1}
.cd div{display:flex;gap:10px;align-items:center}
.cd svg{width:16px;height:16px;fill:var(--red)}
.bottom{height:40px;background:#111;color:#888;font-size:11px}
.bottom .wrap{display:flex;justify-content:space-between;align-items:center;height:40px}
.pay{display:flex;gap:6px}
.pay span{width:36px;height:22px;background:#ddd;border-radius:2px}
</style>
</head>
<body>
<svg width="0" height="0" style="position:absolute"><defs><symbol id="star" viewBox="0 0 24 24"><path d="M12 2l3 7h7l-5.5 4.5 2 7.5-6.5-4.5-6.5 4.5 2-7.5L2 9h7z"/></symbol></defs></svg>

<div class="topbar"><div class="wrap">
  <span class="big">(555) 318-4702</span>
  <div class="nums"><span>Estero: <b>(555) 318-4702</b></span><span>Naples: <b>(555) 726-1059</b></span><span>Bonita Springs: <b>(555) 726-1059</b></span></div>
  <div class="social" aria-label="Chatterly, Quipster, Vidnook, Careerloop, Zorbo+"><span></span><span></span><span></span><span></span><span></span></div>
</div></div>

<header class="header"><div class="wrap">
  <div class="logo"><span class="dot"></span><span class="name">Talvik Crew<br>Plumbing &amp; Drain</span></div>
  <div class="hbtns"><span class="chat">LIVE CHAT WITH<br>EXPERTS</span><span class="btn">24 HR Emergency Plumber</span></div>
</div></header>

<nav class="nav"><div class="wrap"><ul><li>About Talvik Crew</li><li>The Service Areas</li><li>Our Services</li><li>Sewer &amp; Drain Cleaning</li><li>Products</li><li>Blog</li><li>Contact Us</li></ul></div></nav>

<section class="hero" role="img" aria-label="Plumber at work repairing a wall-mounted boiler">
  <div class="cap"><h1>24 Hour Emergency Plumber</h1><p>Our expert plumbing crew is on call around the clock to handle leaks, bursts and blocked lines across the region.</p><span class="btn">24 Hour Emergency Plumber</span></div>
  <div class="dots"><span></span><span></span><span></span></div>
</section>

<section class="ratings"><div class="wrap">
  <div class="rate"><h2 class="sec"><svg class="star"><use href="#star"/></svg>We're Rated A <span class="hl">On Marla's List.</span></h2>
    <div class="row"><span class="badge"></span><span class="badge" style="width:70px;border-radius:50%"></span></div>
    <a>marlaslist.com/review/000000</a><p style="margin-top:8px">Please review us by clicking the logo after your plumbing or drain service today.</p></div>
  <div class="rate"><h2 class="sec"><svg class="star"><use href="#star"/></svg>QTB Accredited <span class="hl">Business</span></h2>
    <div class="row"><span class="badge b"></span><a>Click here for review</a></div>
    <p>We take our A+ rating with the Quality Trade Bureau seriously. We strive for our customers complete satisfaction.</p></div>
</div></section>

<section class="tv"><div class="wrap">
  <div class="col"><h2 class="sec"><svg class="star"><use href="#star"/></svg>Clients <span class="hl">Testimonials</span></h2>
    <div class="tcard"><span class="av" role="img" aria-label="Customer portrait"></span><div><p>“Quick response, fair upfront price and a spotless job. The crew fixed our leaking line the same day and explained every step along the way.”</p><div class="stars">★★★★★</div><div class="who">-Dana Rowe</div></div></div>
    <div class="tcard"><span class="av" role="img" aria-label="Customer portrait"></span><div><p>“Quick response, fair upfront price and a spotless job. The crew fixed our leaking line the same day and explained every step along the way.”</p><div class="stars">★★★★★</div><div class="who">-Dana Rowe</div></div></div>
  </div>
  <div class="col"><h2 class="sec"><svg class="star"><use href="#star"/></svg>Watch <span class="hl">Our Video</span></h2>
    <div class="video" role="img" aria-label="Video still of the company owner speaking"><span class="vtitle">Ft Myers and Naples, FL Plumbing</span><span class="play"></span><span class="vbar"></span></div>
  </div>
</div></section>

<section class="welcome"><div class="wrap">
  <div class="main"><h2>Welcome To</h2><h3>Talvik Crew Plumbing &amp; Drain LLC</h3>
    <p>Welcome to Talvik Crew Plumbing &amp; Drain. We are your premier Fort Myers, San Carlos Park, Estero, Bonita Springs, Naples plumber. We have all of what a company in the past who charged a fee for coming to our door. We know these service charges can make it difficult to obtain a second opinion. They can also make you feel obligated to accept an estimate. That's why we offer 100% no obligation free estimates and upfront pricing. You can rest assured knowing your free estimate can't be beat and you will not pay a penny more than quoted.</p>
    <p>Our upfront pricing lets you know what our plumbing service or drain cleaning service will cost before the work begins. If you accept our free estimate, the work will begin at the agreed upon price. We are a licensed and insured Ft. Myers, San Carlos Park, Estero, Bonita Springs, Naples plumber. Talvik Crew is a veteran owned and operated company and can be trusted to respect your home. Our expert plumbing service and clogged drain cleaning service is available 24 hours a day to serve you when you need us most.</p>
    <span class="ribbon">We offer 24 hour Support!!!</span><br><span class="btn dark">Get More Information</span></div>
  <aside class="form"><h4>Free Estimate</h4><div class="in"><p class="note">We offer 100% no obligation<br><b style="color:var(--red)">FREE ESTIMATES</b> &amp; upfront pricing.</p>
    <div class="field">Enter your first name</div><div class="field">Enter your last name</div><div class="field">Enter your email address</div><div class="field">Enter your phone number</div><div class="field">Enter your address</div><div class="field ta">Enter your message</div><div class="captcha"></div>
    <div style="text-align:center"><span class="btn">Get Free Estimate Now</span></div></div></aside>
</div></section>

<section class="services"><div class="wrap">
  <h2 class="sec" style="justify-content:center"><svg class="star"><use href="#star"/></svg>Our <span class="hl">Services</span></h2>
  <div class="cards">
    <div class="card"><div class="img ph" role="img" aria-label="Sewer and drain cleaning equipment"></div><div class="lbl"><i></i><span>Sewer &amp;<br>Drain Cleaning</span></div></div>
    <div class="card"><div class="img ph" role="img" aria-label="Sewer video inspection"></div><div class="lbl"><i></i><span>Sewer Video<br>Inspections</span></div></div>
    <div class="card"><div class="img ph" role="img" aria-label="Plumber servicing a water heater"></div><div class="lbl"><i></i><span>Water Heater Repair<br>&amp; Installation</span></div></div>
    <div class="card"><div class="img ph" role="img" aria-label="Toilet repair"></div><div class="lbl"><i></i><span>Toilet Repair<br>&amp; Installation</span></div></div>
  </div>
  <div class="center"><span class="btn">View All Services</span></div>
</div></section>

<section class="why"><div class="wrap">
  <h2 class="sec"><svg class="star" style="fill:#fff"><use href="#star"/></svg>Why <span class="hl">Choose Us?</span></h2>
  <div class="cols"><div style="flex:1"><p class="lead">We will arrive on time, meet your budget, clean up before we leave, and warranty our work.</p>
    <ul><li>24 hour emergency service</li><li>Licensed insured uniformed technicians</li><li>Remodeling commercial residential services</li><li>Certified backflow testing installation repair</li><li>Electronic leak detection</li><li>Water heater repair / installation</li><li>Toilet repair / installation</li><li>Faucet repair / installation</li><li>Expert clogged drain cleaning</li><li>Sewer camera inspections</li><li>Sewer blockages located and repaired</li><li>Hydro Jetting services</li></ul>
    <span class="ribbon">We offer 24 hour Support!!!</span></div>
  <div class="vid"><div class="video" role="img" aria-label="Video still of a plumber talking to camera"><span class="vtitle">Our Services any time any where</span><span class="play"></span><span class="vbar"></span></div>
    <p>Talvik Crew Plumbing &amp; Drain is a state licensed and insured plumbing contractor in Fort Myers &amp; Naples, FL. Call us for your residential or commercial plumbing projects.</p></div></div>
</div></section>

<section class="plugins"><div class="wrap">
  <div class="pl"><h5>Find us on Chatterly</h5><div class="it"><i></i><div><b>Talvik Crew Plumbing &amp; Drain LLC</b><br>Like Page</div></div><div style="height:140px;background:#f5f5f5;margin:0 12px"></div></div>
  <div class="pl"><h5>Quipster</h5><div class="it"><i></i><div><b>Talvik Crew</b> @talvikcrew<br>Latest plumbing tips and local service news.</div></div><div class="it"><i></i><div><b>Talvik Crew</b> @talvikcrew<br>Latest plumbing tips and local service news.</div></div></div>
  <div class="pl"><h5>Follow @talvikcrew</h5><div class="it"><i></i><div><b>Talvik Crew</b> @talvikcrew<br>Latest plumbing tips and local service news.</div></div><div class="it"><i></i><div><b>Talvik Crew</b> @talvikcrew<br>Latest plumbing tips and local service news.</div></div></div>
  <div class="pl"><h5>Latest Coupons</h5><div class="it" style="height:170px"><div style="flex:1;background:#f5f5f5"></div></div></div>
</div></section>

<footer class="footer"><div class="wrap">
  <div class="fcol"><h2 class="sec">Services <span class="hl">Area</span></h2><div class="map" role="img" aria-label="Map of southwest Florida service area"></div>
    <div class="areas">Bonita Springs Plumbing<br>Estero Plumbing<br>Fort Myers Plumbing<br>Naples Plumbing<br>San Carlos Park</div></div>
  <div class="fcol"><h2 class="sec">Quick <span class="hl">Contact</span></h2><div class="ff"></div><div class="ff"></div><div class="ff ta"></div><span class="btn">Send</span></div>
  <div class="fcol"><h2 class="sec">Contact <span class="hl">Detail</span></h2><p style="margin-top:12px;line-height:1.6">Proudly serving Fort Myers, Estero, Naples and Bonita Springs.</p>
    <div class="cd"><div><svg viewBox="0 0 24 24"><path d="M12 2a7 7 0 0 0-7 7c0 5 7 13 7 13s7-8 7-13a7 7 0 0 0-7-7zm0 9.5a2.5 2.5 0 1 1 0-5 2.5 2.5 0 0 1 0 5z"/></svg>4810 Harlow Ave, Fort Myers, FL 33900</div>
    <div><svg viewBox="0 0 24 24"><path d="M6.6 10.8a15 15 0 0 0 6.6 6.6l2.2-2.2c.3-.3.7-.4 1-.2 1.1.4 2.3.6 3.6.6.6 0 1 .4 1 1V20c0 .6-.4 1-1 1A17 17 0 0 1 3 4c0-.6.4-1 1-1h3.5c.6 0 1 .4 1 1 0 1.3.2 2.5.6 3.6.1.3 0 .7-.2 1z"/></svg>(555) 318-4702</div>
    <div><svg viewBox="0 0 24 24"><path d="M3 5h18v14H3zm2 2v.5l7 4.5 7-4.5V7z"/></svg>info@talvikcrew.com</div></div></div>
</div></footer>

<div class="bottom"><div class="wrap"><span>Copyright © 2014 Talvik Crew Plumbing &amp; Drain LLC. All Rights Reserved.</span><div class="pay" aria-label="Accepted payment cards"><span></span><span></span><span></span><span></span><span></span></div></div></div>
</body>
</html>
```